Skill Up Salary Up

Full Page
7.5 w x 10 h / 8 w x 10.75 h + .25" bleed
Full-Page Career Course Ad
Project Overview
• Goal: Create a visually attractive, modern, and uncluttered full-page magazine advertisement to list available career courses.
• Tone: Creative, professional, and attention-grabbing to prevent the reader from turning the page. The final design must prioritize readability.

Content Requirements
1. Header/Headline: Must be the primary focus. And grab peoples attention
2. Course Listing: A clear, well-organized list of the career courses.
________________________________________
Design & Aesthetic Directives
1. Layout & Readability (Crucial)
• The final ad must not look crowded or busy.
• Prioritize white space to make the text "breathe" and ensure the course list is easy to scan and read.
• Use a modern, clean, and professional typeface (font choice is critical for the aesthetic).
2. Visual Style
• Aim for a creative, modern, and fresh look. Avoid outdated or generic stock imagery/layouts.
3. Imagery/Graphic Element (Artist's Choice)
You have creative freedom regarding the main graphic element.
• Option A (Photography): Use a photo of a white male American with a collared shirt. The imagery should convey success, focus, or professional development.
• Option B (Vector/Illustration): Use a modern vector graphic, illustration, or abstract design. This could be used to symbolize growth, connection, or a career path.
The choice of graphic element is yours, but it must support the overall modern and uncrowded aesthetic.

Requirements
Must have
• Partial listing .. is part of the Harbor Lantern Course

```html
<!DOCTYPE html>
<html lang="en">
<head>
<meta charset="utf-8">
<title>Skill Up, Salary Up – Upcoming KTR Courses</title>
<link rel="stylesheet" href="https://fonts.googleapis.com/css2?family=Barlow+Semi+Condensed:wght@600;700&family=Montserrat:wght@700&family=Nunito+Sans:wght@400;700;800&display=swap">
<style>
  :root {
    --deep-teal: #184f55;
    --bright-teal: #1a9990;
    --sun: #fbbb45;
    --orange: #f18a2a;
    --ink: #111;
    --paper: #fff;
  }
  * { margin: 0; padding: 0; box-sizing: border-box; }
  html, body { width: 907px; height: 1200px; overflow: hidden; background: var(--paper); }
  .ad { position: relative; width: 907px; height: 1200px; overflow: hidden; font-family: "Nunito Sans", Arial, sans-serif; color: var(--ink); }

  .header-band { position: absolute; left: 0; top: 0; width: 907px; height: 355px; background: var(--deep-teal); }
  .hero-photo { position: absolute; left: 0; top: 0; }
  .headline { position: absolute; left: 56px; top: 30px; font-family: "Barlow Semi Condensed", sans-serif; font-weight: 700; color: var(--sun); font-size: 92px; line-height: 88px; letter-spacing: 0.5px; }
  .subhead { position: absolute; left: 57px; top: 216px; font-family: "Barlow Semi Condensed", sans-serif; font-weight: 700; color: var(--paper); font-size: 41px; line-height: 48px; }
  .tagline { position: absolute; left: 57px; top: 282px; font-family: "Barlow Semi Condensed", sans-serif; font-weight: 600; color: var(--paper); font-size: 20px; }

  .column-rule { position: absolute; width: 2px; background: var(--deep-teal); }
  .block-rule { position: absolute; height: 2px; background: var(--deep-teal); }

  .course { position: absolute; }
  .course h2 { font-family: "Montserrat", sans-serif; font-weight: 700; color: var(--bright-teal); font-size: 29px; line-height: 29px; letter-spacing: -0.2px; }
  .label { font-weight: 800; font-size: 15px; line-height: 20px; }
  .items { list-style: none; font-size: 15.5px; line-height: 19.5px; }
  .items li::before { content: "• "; font-size: 11px; vertical-align: 2px; }
  .accent { color: var(--orange); font-weight: 800; font-size: 16px; line-height: 21px; }
  .schedule { color: var(--orange); font-weight: 800; font-size: 17.5px; line-height: 20px; }
  .note { color: var(--orange); font-weight: 800; font-size: 13.5px; line-height: 18px; }
  .listing-grid { display: grid; grid-template-columns: 142px 110px; margin-left: 2px; }

  .growth-art { position: absolute; left: 640px; top: 811px; width: 234px; height: 208px; border-radius: 4px; background: linear-gradient(160deg, #bfe3e4 0%, #4fa4ae 55%, #1f6f7a 100%); }

  .footer { position: absolute; left: 0; top: 1067px; width: 907px; height: 133px; background: var(--deep-teal); }
  .brand { position: absolute; left: 70px; top: 37px; display: flex; align-items: center; gap: 12px; }
  .brand-square { width: 54px; height: 54px; background: var(--paper); border-radius: 5px; }
  .brand-name { font-family: "Barlow Semi Condensed", sans-serif; font-weight: 600; font-size: 44px; color: var(--paper); }
  .contact { position: absolute; right: 63px; top: 44px; text-align: center; font-family: "Barlow Semi Condensed", sans-serif; font-weight: 600; color: var(--paper); font-size: 16px; line-height: 18px; }
</style>
</head>
<body>
<div class="ad">
  <div class="header-band"></div>
  <svg class="hero-photo" width="907" height="420" viewBox="0 0 907 420" role="img" aria-label="Photo of a smiling professional man in a white collared shirt, arms crossed, in a bright office">
    <defs>
      <linearGradient id="photoTone" x1="0" y1="0" x2="1" y2="1">
        <stop offset="0" stop-color="#e6ece6"/>
        <stop offset="0.5" stop-color="#d9ddd6"/>
        <stop offset="1" stop-color="#8fa889"/>
      </linearGradient>
    </defs>
    <path d="M516 0 H907 V320 C840 385 730 405 640 392 C605 386 585 372 570 355 H646 Z" fill="url(#photoTone)"/>
  </svg>

  <div class="headline">SKILL UP,<br>SALARY UP</div>
  <div class="subhead">UPCOMING KTR COURSES</div>
  <div class="tagline">Men &amp; Women • In-Person &amp; Remote • Partial Scholarships</div>

  <div class="column-rule" style="left:322px;top:403px;height:625px"></div>
  <div class="column-rule" style="left:617px;top:410px;height:625px"></div>
  <div class="block-rule" style="left:52px;top:768px;width:223px"></div>
  <div class="block-rule" style="left:345px;top:707px;width:223px"></div>

  <section class="course" style="left:53px;top:408px;width:265px">
    <h2>Harbor Lantern<br>Course</h2>
    <p class="label" style="margin-top:11px">Business Skills &amp; Knowledge to:</p>
    <ul class="items" style="margin-top:4px">
      <li>Impress your interviewer</li>
      <li>Maximize income</li>
      <li>Start / Run your business</li>
    </ul>
    <p class="label" style="margin-top:13px">Partial Listing:</p>
    <div class="listing-grid" style="margin-top:7px">
      <ul class="items"><li>Computers</li><li>Marketing</li><li>Sales</li><li>Finance</li><li>Healthcare</li><li>Communication</li></ul>
      <ul class="items"><li>Business<br>&nbsp;&nbsp;Strategy</li><li>LedgerLeaf</li><li>Investments</li><li>Real Estate</li><li>Accounting</li></ul>
    </div>
    <p class="schedule" style="margin-top:12px">Nov 2025 • 4 - 5 Months</p>
  </section>

  <section class="course" style="left:53px;top:792px;width:265px">
    <h2>Bookkeeping<br>LedgerLeaf</h2>
    <ul class="items accent" style="margin-top:12px;line-height:19.5px"><li>Train for a quality job</li><li>Manage your own books</li></ul>
    <p class="label" style="margin-top:12px">Skills:</p>
    <ul class="items" style="margin-top:2px"><li>Finance Management</li><li>Customer &amp; Vendor Management</li><li>Advanced Tools</li></ul>
    <p class="schedule" style="margin-top:9px">Nov 2025 • 5 Weeks</p>
  </section>

  <section class="course" style="left:345px;top:409px;width:265px">
    <h2>Software,<br>Web &amp; Apps</h2>
    <p class="accent" style="margin-top:8px">#2 Best Tech Job –<br>National Careers Review 2025</p>
    <p class="label" style="margin-top:12px">Job Opportunities:</p>
    <ul class="items" style="margin-top:5px"><li>Computer Programmer</li><li>Software Developer / Mobile</li><li>Engineer Developer (Apps)</li></ul>
    <p class="schedule" style="margin-top:11px">Nov 2025</p>
    <p class="note" style="margin-top:6px">Optional: Bachelor’s in Programming<br>&amp; Tech</p>
  </section>

  <section class="course" style="left:345px;top:733px;width:265px">
    <h2>IT Desktop &amp;<br>Networking<br>Support</h2>
    <p class="accent" style="margin-top:13px">#2 Best Tech Job –<br>National Careers Review 2025</p>
    <p class="label" style="margin-top:12px">Skills:</p>
    <ul class="items" style="margin-top:2px"><li>Desktop Systems</li><li>Networks</li><li>Servers</li><li>Cloud</li></ul>
    <p class="schedule" style="margin-top:8px">Dec 2025 • 7 Months</p>
  </section>

  <section class="course" style="left:642px;top:468px;width:255px">
    <h2>Office Suite –<br>Computers</h2>
    <p class="accent" style="margin-top:11px">The New Job Prerequisite</p>
    <p class="label" style="margin-top:12px">Skills:</p>
    <ul class="items" style="margin-top:2px"><li>Spreadsheets</li><li>Documents</li><li>Email &amp; Calendar</li><li>Presentations</li></ul>
    <p class="schedule" style="margin-top:8px">Dec 2025 • 5 Weeks</p>
    <p class="note" style="margin-top:8px">Note: Computer lab available to<br>practice</p>
  </section>

  <div class="growth-art" role="img" aria-label="Illustration of rising arrows and a staircase with people climbing toward success"></div>

  <footer class="footer">
    <div class="brand"><div class="brand-square"></div><span class="brand-name">Stridewell Co</span></div>
    <div class="contact">Contact Us:<br>administrator@stridewell.example</div>
  </footer>
</div>
</body>
</html>
```